Marlow Ridge Infirmary College of Nursing

We need to overhaul a website we've previously used (mrcnalumni.org) which I as administrator am no longer able to edit. There is a general history of the school which can be still used. We would like tabs for membership rosters, news and updates, scholarship information, Board of Directors information, and a chat page that is easy to use. All of our members are over 70 years of age, so simplicity is important.

```html
<!DOCTYPE html>
<html lang="en">
<head>
<meta charset="utf-8">
<title>Contact Us — Marlow Ridge Infirmary College of Nursing</title>
<link rel="stylesheet" href="https://fonts.googleapis.com/css2?family=Crimson+Pro:wght@600;700&display=swap">
<style>
  :root {
    --brand-blue: #00419a;
    --brand-gold: #f9c85a;
    --required-red: #e3211c;
    --page-white: #ffffff;
    --photo-dark: #3c3c3c;
    --photo-mid: #8a8a8a;
    --photo-light: #d8d8d8;
    --photo-edge: #9a9a9a;
  }
  * { box-sizing: border-box; margin: 0; padding: 0; }
  html, body { width: 1200px; height: 675px; overflow: hidden; background: var(--page-white); }
  body { font-family: "Crimson Pro", Georgia, serif; color: var(--brand-blue); }
  .canvas { position: relative; width: 1200px; height: 675px; overflow: hidden; }

  .site-header { position: absolute; left: 0; top: 0; width: 1200px; height: 150px; background: var(--brand-blue); }
  .nav-group { position: absolute; top: 98px; display: flex; justify-content: space-around; align-items: baseline; }
  .nav-left { left: 20px; width: 470px; }
  .nav-right { left: 705px; width: 485px; justify-content: space-between; }
  .nav-link { color: var(--page-white); font-weight: 700; font-size: 18px; line-height: 1.2; text-decoration: none; white-space: nowrap; }

  .brand { position: absolute; left: 500px; top: 14px; width: 200px; text-align: center; }
  .brand-dot { display: block; width: 44px; height: 44px; margin: 0 auto 8px; border-radius: 50%; background: var(--brand-gold); }
  .brand-name { color: var(--page-white); font-weight: 700; font-size: 17px; line-height: 1.1; }

  .page-title { position: absolute; left: 78px; top: 166px; font-weight: 700; font-size: 76px; line-height: 1; letter-spacing: -0.5px; white-space: nowrap; }

  .field-label { position: absolute; font-weight: 700; font-size: 19px; line-height: 1; white-space: nowrap; }
  .field-label .required { color: var(--required-red); }
  .field-input { position: absolute; border: 4px solid var(--brand-blue); background: var(--page-white); resize: none; }

  .label-first { left: 61px; top: 273px; }
  .input-first { left: 58px; top: 295px; width: 171px; height: 35px; }
  .label-last { left: 263px; top: 274px; }
  .input-last { left: 259px; top: 295px; width: 171px; height: 35px; }
  .label-email { left: 60px; top: 345px; }
  .input-email { left: 61px; top: 365px; width: 171px; height: 35px; }
  .label-message { left: 263px; top: 348px; }
  .input-message { left: 260px; top: 368px; width: 283px; height: 147px; }

  .submit-button { position: absolute; left: 61px; top: 442px; width: 146px; height: 58px; border-radius: 29px; background: var(--brand-blue); color: var(--page-white); font-family: "Crimson Pro", Georgia, serif; font-weight: 700; font-size: 21px; border: none; }

  .archive-photo { position: absolute; left: 678px; top: 218px; width: 474px; height: 351px; border: 1px solid var(--photo-edge);
    background: linear-gradient(160deg, var(--photo-dark) 0%, var(--photo-mid) 45%, var(--photo-light) 70%, var(--photo-mid) 100%); }
</style>
</head>
<body>
<div class="canvas">
  <header class="site-header">
    <nav class="nav-group nav-left" aria-label="Primary">
      <a class="nav-link" href="#">About Us</a>
      <a class="nav-link" href="#">Member Portal</a>
      <a class="nav-link" href="#">Scholarships</a>
    </nav>
    <div class="brand">
      <span class="brand-dot"></span>
      <div class="brand-name">Marlow Ridge Infirmary<br>College of Nursing</div>
    </div>
    <nav class="nav-group nav-right" aria-label="Secondary">
      <a class="nav-link" href="#">Board of Directors</a>
      <a class="nav-link" href="#">Chat</a>
      <a class="nav-link" href="#">Contact Us</a>
      <a class="nav-link" href="#">News &amp; Updates</a>
    </nav>
  </header>

  <h1 class="page-title">Contact Us</h1>

  <form class="contact-form">
    <label class="field-label label-first" for="first-name">first name<span class="required">*</span></label>
    <input class="field-input input-first" id="first-name" type="text">
    <label class="field-label label-last" for="last-name">last name<span class="required">*</span></label>
    <input class="field-input input-last" id="last-name" type="text">
    <label class="field-label label-email" for="email">email<span class="required">*</span></label>
    <input class="field-input input-email" id="email" type="email">
    <label class="field-label label-message" for="message">message</label>
    <textarea class="field-input input-message" id="message"></textarea>
    <button class="submit-button" type="button">submit</button>
  </form>

  <div class="archive-photo" role="img" aria-label="Black-and-white archival photograph of four nursing students in uniforms walking outside the hospital building"></div>
</div>
</body>
</html>
```